Digital Album Cover - Piano music for wedding ceremonies and receptions

I need cover art for a piano album project that will be distributed to TuneVault, Wavelane etc. Covert art required for front of album. At this stage physical CDs will not be printed nor required it is just a digital release.
Artist name: Toby Hargrove
Album Title: Gentle Keys Melodies Wedding Ceremonies and Receptions
Volume 3
Sample piano songs are on my tunecast page
https://tunecast.example/tobyhargrovekeys/sets/gentle-keys-melodies-vol-3
Previous album artwork used from sketch hive competitions winners
https://musicvault.example/au/artist/toby-hargrove/4830917265
Target Market(s)
brides to be
grooms to be
people interested in weddings
people enjoy love songs or easy listening music
Industry/Entity Type
Wedding
Look and feel
Each slider illustrates characteristics of the customer's brand and the style your logo design should communicate.

```html
<!DOCTYPE html>
<html lang="en">
<head>
<meta charset="utf-8">
<title>Toby Hargrove – Gentle Keys Melodies Vol. 3</title>
<link rel="stylesheet" href="https://fonts.googleapis.com/css2?family=Libre+Baskerville:wght@400;700&family=Mrs+Saint+Delafield&display=swap">
<style>
  :root {
    --stage: #0c0c0c;
    --paper: #ffffff;
    --gold: #d79a62;
    --gold-soft: #dcae80;
    --script: #ee9a45;
    --rule: #f3d9d6;
    --photo-light: #fdeedd;
    --photo-warm: #f0c39c;
    --photo-skin: #e4a88f;
    --photo-rose: #d4a097;
    --photo-key: #e9c3ad;
  }
  * { margin: 0; padding: 0; box-sizing: border-box; }
  html, body {
    width: 1200px; height: 720px; overflow: hidden;
    background: var(--stage);
  }
  .stage { position: relative; width: 1200px; height: 720px; }
  .album-cover {
    position: absolute; left: 289px; top: 52px;
    width: 607px; height: 607px;
    background: var(--paper); overflow: hidden;
  }
  .cover-photo {
    position: absolute; left: 0; right: 0; top: 200px; bottom: 0;
    background:
      radial-gradient(ellipse 28% 55% at 8% 30%, rgba(255,255,255,0.95) 0%, rgba(255,255,255,0) 100%),
      radial-gradient(ellipse 30% 40% at 42% 68%, rgba(228,168,143,0.85) 0%, rgba(228,168,143,0) 100%),
      radial-gradient(ellipse 40% 30% at 80% 48%, rgba(232,170,130,0.85) 0%, rgba(232,170,130,0) 100%),
      radial-gradient(ellipse 22% 40% at 96% 15%, rgba(240,180,130,0.8) 0%, rgba(240,180,130,0) 100%),
      radial-gradient(ellipse 45% 32% at 48% 18%, var(--paper) 0%, rgba(255,255,255,0.9) 50%, rgba(255,255,255,0) 100%),
      linear-gradient(180deg, var(--photo-light) 0%, var(--photo-warm) 45%, var(--photo-key) 70%, var(--photo-rose) 100%);
    -webkit-mask-image: linear-gradient(180deg, transparent 0%, #000 22%);
            mask-image: linear-gradient(180deg, transparent 0%, #000 22%);
  }
  .cover-text {
    position: absolute; left: 0; right: 0; top: 0;
    text-align: center; color: var(--gold-soft);
  }
  .artist-name {
    position: absolute; left: 14px; right: 0; top: 34px;
    font-family: "Libre Baskerville", Georgia, serif;
    font-size: 12.5px; letter-spacing: 5.4px; color: var(--gold);
  }
  .album-title {
    position: absolute; left: 20px; right: 0; top: 58px;
    font-family: "Mrs Saint Delafield", cursive;
    font-size: 64px; line-height: 1; font-weight: 400; color: var(--script);
  }
  .album-subtitle {
    position: absolute; left: 0; right: 0; top: 132px;
    font-family: "Libre Baskerville", Georgia, serif;
    font-weight: 700; font-size: 16.5px; line-height: 20px;
  }
  .album-subtitle .amp { font-size: 9px; vertical-align: 6px; margin-right: 4px; }
  .title-rule {
    position: absolute; left: 260px; top: 183px;
    width: 100px; height: 1px; background: var(--rule);
  }
  .volume {
    position: absolute; left: 6px; right: 0; top: 193px;
    font-family: "Libre Baskerville", Georgia, serif;
    font-weight: 700; font-size: 17px;
  }
</style>
</head>
<body>
  <main class="stage">
    <section class="album-cover">
      <div class="cover-photo" role="img" aria-label="Sunlit photograph of a bride's and groom's hands with wedding rings touching on piano keys"></div>
      <div class="cover-text">
        <p class="artist-name">TOBY HARGROVE</p>
        <h1 class="album-title">Gentle Keys Melodies</h1>
        <p class="album-subtitle">Wedding Ceremonies<br><span class="amp">&amp;</span>Receptions</p>
        <div class="title-rule"></div>
        <p class="volume">Vol. 3</p>
      </div>
    </section>
  </main>
</body>
</html>
```